依頼詳細
新商品発売に合わせてチラシを作成し、一般客や販売先の量販店、小売店等に配布したいと思います。
当社は老舗の部類に入り、近隣では相応の知名度を有しています。看板商品は高級品路線です。ブランドイメージもそこそこあります。それをあまり逸脱しないような感じでお願いします。
POP過ぎる物は難しいかもしれません。

自社製品を製造・販売している部門はいつもこういった販促素材を活用していますが、当部門では初めてで、このような依頼も初めてになります。
不慣れな部分もあると思いますがよろしくお願いします。
記載項目
〇社名 鳴瀬水産食品株式会社 商品事業部
〇電話番号 0790-41-3876
〇FAX 0790-48-1629
〇URL  https://www.naruse-yamaichi.co.jp/
サイズ
A4
ページ数
片面
希望イメージ
シンプル 複雑
単色 カラフル
暗い 明るい
日常 高級
遊び心 厳粛
未来的 伝統的
女性的 男性的
希望する色
納品ファイル
補足説明
■ 選んだ理由

複数の社員により選択されました。
使用イメージ画像も多く、また弊社看板製品も掲載していただいており、非常に分かり易いとの評価でした。
色使いがカラフルとの声もありました。

■ 提案者全員のお礼・コメント

今回初挑戦で不慣れな点も多く、なかなかスムーズにいかなくてご迷惑をお掛けした部分もあったと思いますが、思いもかけず多数のご提案をいただき、大変ありがたかったです。
また何かでお願いすることもあると思いますので、今後ともよろしくお願いいたします。

```html
<!DOCTYPE html>
<html lang="ja">
<head>
<meta charset="utf-8">
<title>焼小鯛だし 新発売</title>
<link rel="stylesheet" href="https://fonts.googleapis.com/css2?family=Shippori+Mincho:wght@400;600;800&family=Noto+Serif+JP:wght@400;600&display=swap">
<style>
  :root{
    --cream:#f1ece0;
    --paper:#fbf9f4;
    --ink:#2a2a2a;
    --red:#c8252c;
    --navy:#1f3f68;
    --gold:#b8a47a;
    --wave:#3d6a92;
  }
  *{margin:0;padding:0;box-sizing:border-box}
  html,body{width:849px;height:1200px;overflow:hidden;background:var(--cream)}
  .flyer{position:relative;width:849px;height:1200px;background:var(--cream);font-family:"Shippori Mincho","Noto Serif JP",serif;color:var(--ink);overflow:hidden}
  .pattern-bg{position:absolute;inset:0;background:linear-gradient(180deg,#efe9dc 0%,#f3eee3 60%,#ece5d6 100%)}
  .center-panel{position:absolute;left:185px;top:0;width:495px;height:820px;background:var(--paper);border-left:2px solid var(--gold);border-right:2px solid var(--gold)}
  .center-panel::before,.center-panel::after{content:"";position:absolute;top:0;bottom:0;width:1px;background:var(--gold)}
  .center-panel::before{left:6px}.center-panel::after{right:6px}
  .brand{position:absolute;left:0;width:849px;top:34px;text-align:center;font-size:26px;font-weight:800;letter-spacing:14px;color:var(--ink)}
  .brand-dot{display:inline-block;width:22px;height:22px;border-radius:50%;background:var(--navy);vertical-align:-3px;margin-right:10px}
  .badge{position:absolute;left:236px;top:128px;width:30px;padding:8px 0;background:var(--red);color:#fff;writing-mode:vertical-rl;font-size:16px;font-weight:600;letter-spacing:4px;display:flex;align-items:center;justify-content:center;border-radius:3px}
  .title{position:absolute;left:268px;top:150px;writing-mode:vertical-rl;font-size:54px;font-weight:800;letter-spacing:4px;line-height:1}
  .fish-art{position:absolute;left:450px;top:70px;width:210px;height:200px;border-radius:50%;background:radial-gradient(circle at 45% 50%,#e89a94 0%,#f0c2bc 55%,rgba(251,249,244,0) 72%)}
  .story{position:absolute;left:432px;top:282px;width:228px;height:305px;writing-mode:vertical-rl;font-size:14px;line-height:28px;letter-spacing:1px;white-space:nowrap;overflow:hidden}
  .dish-photo{position:absolute;left:170px;top:605px;width:525px;height:355px;border-radius:6px;background:radial-gradient(ellipse at 50% 45%,#d8b58a 0%,#a86b3a 30%,#6a3b1e 55%,#3a2418 80%,#2c2420 100%)}
  .waves{position:absolute;left:0;top:820px;width:849px;height:240px;background:linear-gradient(180deg,#a7bfd4 0%,#5c86ab 45%,var(--wave) 100%)}
  .pack-photo{position:absolute;left:55px;top:820px;width:170px;height:235px;border-radius:4px;background:linear-gradient(160deg,#f4f4f2 0%,#e9e2d5 35%,#e07a2c 60%,#c8461f 100%);box-shadow:0 2px 6px rgba(0,0,0,.15)}
  .footer{position:absolute;left:0;top:1060px;width:849px;height:140px;background:var(--paper);display:flex;justify-content:space-between;padding:24px 70px 0 55px}
  .product-name{font-size:22px;font-weight:600;margin-bottom:8px}
  .product-spec{font-size:12px;line-height:20px}
  .company{text-align:left;font-size:13px;line-height:20px}
  .company-name{font-size:17px;font-weight:600}
  .company-name small{font-size:12px;margin-left:12px;font-weight:400}
  .tel{font-size:20px;font-weight:600;color:var(--navy);line-height:28px}
  .tel span{font-size:13px;color:var(--ink);font-weight:400;margin-left:10px}
  .url{font-family:"Noto Serif JP",serif;font-size:13px}
</style>
</head>
<body>
<div class="flyer">
  <div class="pattern-bg" role="img" aria-label="淡い和柄の背景（青海波・扇・雲の文様）"></div>
  <div class="center-panel"></div>

  <div class="brand"><span class="brand-dot"></span>鳴瀬</div>

  <div class="badge">新発売</div>
  <h1 class="title">焼小鯛だし</h1>

  <div class="fish-art" role="img" aria-label="跳ねる鯛の挿絵"></div>

  <p class="story">お料理のおいしさはだしで決まります。<br>私達は、おだしの素材とレシピに<br>こだわり、じっくりと焼き上げた<br>小鯛を使用しました。小鯛の焼き<br>風味を活かし、かつおとの豊かな<br>香りと旨みです。塩分は控えめに。<br>毎日のお味噌汁、煮物、うどんなど<br>いろいろな料理にご活用ください。</p>

  <div class="dish-photo" role="img" aria-label="小鯛と三つ葉のお吸い物の写真"></div>

  <div class="waves" role="img" aria-label="青い波の文様"></div>
  <div class="pack-photo" role="img" aria-label="焼小鯛だしの商品パッケージ写真"></div>

  <footer class="footer">
    <div class="product">
      <div class="product-name">焼小鯛だし</div>
      <div class="product-spec">70g（7g×10袋入）小鯛だしパック<br>希望小売価格 500円（税抜）</div>
    </div>
    <div class="company">
      <div class="company-name">鳴瀬水産食品株式会社<small>商品事業部</small></div>
      <div>〒670-0941 兵庫県姫路市汐見町2丁目5-1</div>
      <div class="tel">TEL.0790-41-3876<span>FAX.0790-48-1629</span></div>
      <div class="url">https://www.naruse-yamaichi.co.jp/</div>
    </div>
  </footer>
</div>
</body>
</html>
```